The Velvet Heron Espresso Nook Coffee Card

would like a coffee card designed for our café. Most cards are so boring and I need to stand out from the crowd (The Velvet Heron ). I require our logo on one side or the business name also a place for people to write their name and mobile number (collecting data base) and on the back the following
customer gets a stamp for the 1st three coffees purchased, on the 3rd one they get a free upsize. another 2 stamps and on the 3rd one (6) gets a free coffee, another 2 stamps and the customer gets another upsize (9th coffee purchased) and on the 10th card they recivie a voucher for a free pizza.
small print | one free pizza for dinner dining (not available for takeaways and must book), Cant be used with any other offers, opts in to hear from the herd if there is a deal on. cant trade for cash or gift

```html
<!DOCTYPE html>
<html lang="en">
<head>
<meta charset="utf-8">
<title>The Velvet Heron Espresso Nook – Coffee Card</title>
<link rel="stylesheet" href="https://fonts.googleapis.com/css2?family=Teko:wght@500;600&family=Roboto:wght@400;500;700&family=Roboto+Condensed:wght@500;700&display=swap">
<style>
  :root {
    --bg: #d6d6d4;
    --card-dark: #2c2c2c;
    --card-light: #f2f2f0;
    --ink: #1c1c1c;
    --white: #ffffff;
    --rule: #9a9a9a;
    --pizza-orange: #e98a2b;
    --pizza-deep: #d9622a;
    --badge-text: #f0a04b;
  }
  * { box-sizing: border-box; margin: 0; padding: 0; }
  html, body { width: 1125px; height: 1200px; overflow: hidden; }
  body { background: var(--bg); font-family: "Roboto", sans-serif; position: relative; }

  .card { position: absolute; left: 130px; width: 720px; height: 495px; }
  .card__shape { position: absolute; inset: 0; border-radius: 48px; }
  .card--front { top: 100px; }
  .card--front .card__shape { background: var(--card-dark); }
  .card--back { top: 630px; }
  .card--back .card__shape { background: var(--card-light); }

  .brand-title {
    position: absolute; left: 0; right: 0; top: 74px; text-align: center; white-space: nowrap;
    font-family: "Teko", sans-serif; font-weight: 600; font-size: 72px; line-height: 1;
    color: var(--white);
  }
  .brand-rule { position: absolute; left: 168px; width: 414px; top: 157px; height: 2px; background: var(--rule); }
  .brand-sub {
    position: absolute; left: 0; right: 0; top: 168px; text-align: center; white-space: nowrap;
    font-size: 25px; line-height: 30px; color: var(--white); letter-spacing: 0.5px;
  }
  .name-field {
    position: absolute; left: 116px; width: 516px; top: 226px; height: 35px;
    background: var(--white); border-radius: 18px;
    font-family: "Roboto Condensed", sans-serif; font-weight: 500; font-size: 17px;
    color: var(--ink); padding-left: 16px; line-height: 35px; white-space: nowrap;
  }
  .social {
    position: absolute; left: 0; right: 0; top: 300px;
    display: flex; justify-content: center; align-items: center; gap: 8px;
    color: var(--white); font-size: 17px; font-weight: 500; white-space: nowrap;
  }
  .social__dot { width: 12px; height: 12px; border-radius: 50%; background: var(--white); }

  .stamps { position: absolute; left: 0; top: 0; }

  .back-logo { position: absolute; left: 395px; top: 55px; width: 240px; text-align: center; }
  .back-logo__title {
    font-family: "Teko", sans-serif; font-weight: 600; font-size: 31px; line-height: 1;
    color: var(--ink); white-space: nowrap;
  }
  .back-logo__rule { height: 1px; background: var(--rule); margin: 1px 22px 4px; }
  .back-logo__sub { font-size: 11px; line-height: 13px; color: var(--ink); letter-spacing: 0.3px; white-space: nowrap; }

  .pizza-badge { position: absolute; left: 440px; top: 122px; }

  .small-print {
    position: absolute; left: 0; right: 0; top: 280px; text-align: center;
    font-size: 12.5px; line-height: 14.5px; color: var(--ink);
  }
</style>
</head>
<body>

<section class="card card--front" aria-label="Card front">
  <div class="card__shape" role="img" aria-label="Dark sheep-shaped die-cut card silhouette"></div>
  <h1 class="brand-title">THE VELVET HERON</h1>
  <div class="brand-rule"></div>
  <p class="brand-sub">ESPRESSO NOOK</p>
  <div class="name-field">NAME &amp; MOBILE NO:</div>
  <div class="social"><span class="social__dot"></span>@velvetheron</div>
</section>

<section class="card card--back" aria-label="Card back">
  <div class="card__shape" role="img" aria-label="Light sheep-shaped die-cut card silhouette"></div>

  <svg class="stamps" width="720" height="300" viewBox="0 0 720 300">
    <defs>
      <g id="mug-sm">
        <path d="M0 0 H46 V30 Q46 46 30 46 H16 Q0 46 0 30 Z" fill="#1c1c1c"/>
        <path d="M46 6 H52 Q59 6 59 14 V18 Q59 26 52 26 H46" fill="none" stroke="#1c1c1c" stroke-width="5"/>
      </g>
      <g id="mug-lg">
        <path d="M0 0 H62 V42 Q62 62 42 62 H20 Q0 62 0 42 Z" fill="#1c1c1c"/>
        <path d="M62 7 H70 Q79 7 79 17 V22 Q79 32 70 32 H62" fill="none" stroke="#1c1c1c" stroke-width="6"/>
      </g>
    </defs>
    <g font-family="Roboto Condensed, sans-serif" font-weight="700" fill="#fff" text-anchor="middle">
      <use href="#mug-sm" x="135" y="57"/><text x="158" y="86" font-size="14">1</text>
      <use href="#mug-sm" x="228" y="57"/><text x="251" y="86" font-size="14">2</text>
      <use href="#mug-lg" x="310" y="51"/>
      <text x="341" y="81" font-size="21">FREE</text><text x="341" y="95" font-size="12">UPSIZE</text>

      <use href="#mug-sm" x="135" y="137"/><text x="158" y="166" font-size="14">4</text>
      <use href="#mug-sm" x="228" y="137"/><text x="251" y="166" font-size="14">5</text>
      <use href="#mug-lg" x="310" y="130"/>
      <text x="341" y="160" font-size="21">FREE</text><text x="341" y="174" font-size="12">COFFEE</text>

      <use href="#mug-sm" x="135" y="210"/><text x="158" y="239" font-size="14">7</text>
      <use href="#mug-sm" x="228" y="210"/><text x="251" y="239" font-size="14">8</text>
      <use href="#mug-sm" x="318" y="210"/><text x="341" y="239" font-size="14">9</text>
    </g>
  </svg>

  <div class="back-logo">
    <div class="back-logo__title">THE VELVET HERON</div>
    <div class="back-logo__rule"></div>
    <div class="back-logo__sub">ESPRESSO NOOK</div>
  </div>

  <svg class="pizza-badge" width="150" height="150" viewBox="0 0 150 150">
    <defs>
      <path id="badge-arc" d="M35 128 A62 62 0 1 1 128 100"/>
    </defs>
    <circle cx="75" cy="75" r="48" fill="var(--pizza-orange)" role="img" aria-label="Pizza illustration"/>
    <circle cx="75" cy="75" r="40" fill="var(--pizza-deep)" opacity="0.35"/>
    <text font-family="Roboto Condensed, sans-serif" font-weight="700" font-size="13" fill="var(--badge-text)" letter-spacing="1">
      <textPath href="#badge-arc">10TH CARD THEY RECIVIE A VOUCHER FOR A</textPath>
    </text>
    <g font-family="Teko, sans-serif" font-weight="600" text-anchor="middle" fill="#111">
      <text x="73" y="73" font-size="30">FREE</text>
      <text x="75" y="97" font-size="30">PIZZA</text>
    </g>
  </svg>

  <p class="small-print">
    One free pizza for dinner dining (not available for takeaways and must book),<br>
    Cant be used with any other offers • Opts in to hear from the herd if there is a deal on.<br>
    Cant trade for cash or gift
  </p>
</section>

</body>
</html>
```